Business Card for Multi-Brand Sportswear Company

We are looking for a business card which represents our company and the multiple brands within it.

The company: Kelvo Athletics (LTD)
The brands: Kelv, TaliMati, VerdantFlex, Grit and Grime

Employees using these cards would be representing Kelvo Athletics, rather than any of the individual brands. You will see a current design within the uploaded files, to give some inspiration. The actual text of the brands is not necessary, but the logos should be on there is some format.

Our creative minds on this are stretched, so we are looking for someone to make this their own, and show us what a good business card should look like.

We may like to get these printed with spot gloss, so keep that in mind with your designs.

www.kelvoathletics.co.uk

Industry/Entity Type

Business

Contact Information for Business Card

Tom Pennington-Hale
Operations Manager
(+44) 1632 960 417
Tom@kelvoathletics.co.uk
www.kelvoathletics.co.uk

Font styles to use
Sans Serif
Other font styles liked:
• Eurostile

Colors
ffffff

Requirements
Nice to have
• Dark (black) background

```html
<!DOCTYPE html>
<html lang="en">
<head>
<meta charset="utf-8">
<title>Kelvo Athletics – Business Card</title>
<link rel="stylesheet" href="https://fonts.googleapis.com/css2?family=Open+Sans:wght@400;600;700&display=swap">
<style>
  :root {
    --backdrop: #3b3b3b;
    --card: #ffffff;
    --brand-red: #ec1c24;
    --ink: #111111;
    --muted: #8a8a8a;
    --white: #ffffff;
  }
  * { box-sizing: border-box; margin: 0; padding: 0; }
  html, body {
    width: 1105px; height: 1200px; overflow: hidden;
    background: var(--backdrop);
    font-family: "Open Sans", Arial, sans-serif;
  }
  .card {
    position: absolute; left: 196px;
    width: 720px; height: 413px;
    background: var(--card);
    overflow: hidden;
  }
  .card--front { top: 145px; }
  .card--back { top: 602px; }

  .front-swoosh { position: absolute; inset: 0; width: 720px; height: 413px; }

  .wordmark {
    font-weight: 700; color: var(--ink); letter-spacing: 0.5px; white-space: nowrap;
  }
  .card--front .wordmark {
    position: absolute; left: 52px; top: 72px; font-size: 30px;
  }
  .card--back .wordmark {
    position: absolute; left: 0; right: 0; top: 150px;
    text-align: center; font-size: 58px;
  }

  .contact {
    position: absolute; right: 46px; top: 160px;
    text-align: right; color: var(--white);
  }
  .contact__name { font-size: 27px; font-weight: 700; line-height: 36px; }
  .contact__role { font-size: 20px; line-height: 28px; margin-bottom: 12px; }
  .contact__address { font-size: 19px; line-height: 26px; margin-bottom: 12px; }
  .contact__line {
    display: flex; justify-content: flex-end; align-items: center; gap: 8px;
    font-size: 18px; line-height: 28px;
  }
  .contact__icon { width: 18px; height: 18px; fill: var(--white); }

  .brand-row {
    position: absolute; left: 0; right: 0; top: 325px;
    display: flex; justify-content: center; align-items: center; gap: 26px;
  }
  .brand-row__item {
    font-size: 17px; font-weight: 600; color: var(--muted); white-space: nowrap;
  }
</style>
</head>
<body>

<section class="card card--front">
  <svg class="front-swoosh" viewBox="0 0 720 413" aria-hidden="true">
    <path d="M236 413 L431 40 Q452 0 496 0 L720 0 L720 413 Z" fill="var(--ink)"/>
    <path d="M247 413 L442 40 Q463 0 507 0 L720 0 L720 413 Z" fill="var(--white)"/>
    <path d="M256 413 L451 40 Q472 0 516 0 L720 0 L720 413 Z" fill="var(--brand-red)"/>
  </svg>

  <div class="wordmark">Kelvo Athletics</div>

  <div class="contact">
    <div class="contact__name">Tom Pennington-Hale</div>
    <div class="contact__role">Operations Manager</div>
    <div class="contact__address">Fenwick Lane, Ardley<br>Holbrook, ZZ9 4QT</div>
    <div class="contact__line">+44 (0)1632 960417
      <svg class="contact__icon" viewBox="0 0 24 24"><path d="M6.6 10.8a15 15 0 0 0 6.6 6.6l2.2-2.2c.3-.3.7-.4 1-.2 1.1.4 2.3.6 3.6.6.6 0 1 .4 1 1V20c0 .6-.4 1-1 1A17 17 0 0 1 3 4c0-.6.4-1 1-1h3.5c.6 0 1 .4 1 1 0 1.3.2 2.5.6 3.6.1.3 0 .7-.2 1z"/></svg>
    </div>
    <div class="contact__line">tom@kelvoathletics.co.uk
      <svg class="contact__icon" viewBox="0 0 24 24"><path d="M2 5h20v14H2z M2 5l10 8 10-8" fill="none" stroke="#fff" stroke-width="0"/><path d="M2 6v12h20V6l-10 7z"/><path d="M2.5 5h19L12 12z"/></svg>
    </div>
    <div class="contact__line">www.kelvoathletics.co.uk
      <svg class="contact__icon" viewBox="0 0 24 24"><circle cx="12" cy="12" r="10"/><path d="M8 7c2 0 3 1 2 3s2 2 1 4-3 1-3 3M15 5c0 2 2 2 3 4s-1 3 0 5" stroke="var(--brand-red)" stroke-width="1.6" fill="none"/></svg>
    </div>
  </div>
</section>

<section class="card card--back">
  <div class="wordmark">Kelvo Athletics</div>
  <div class="brand-row">
    <span class="brand-row__item">TaliMati</span>
    <span class="brand-row__item">VerdantFlex</span>
    <span class="brand-row__item">Grit and Grime</span>
    <span class="brand-row__item">Kelv</span>
  </div>
</section>

</body>
</html>
```